Professional Website for Commercial Real Estate Broker

I own a small boutique commercial real estate company called Harbinridge Realty.
My current website is www.movewithquorl.com and is hosted on hostelmira. I am looking for an all new website that will allow me to compete with bigger players in our industry. In other words, I need something professional, sleek, and functional.

I am looking for a designer that can take my complete website all the way to coding, migration, and launch. I understand that this may be an add'l charge, so please include with your design submission what the add'l charge will be to take the website to launch with all functionality as described below.

As an example of a page in my industry that I like please check out: www.tobiaskellner.com.

My logo is attached and my main colors are the blue, white, grey - similar to the logo.

I am looking for a five page website with the following pages:

Home
Harbinridge Team
Services
Sold Properties
Contact

A couple of features that I will want on the site are:

- I want to make sure that we can imbed a news commercial real estate news feed from: http://www.bizplotwire.com/news/ on the website's home page, similar to how it is on tobiaskellner.com.

- Sold Properties page will allow me to upload the following information on to the website so that I can add new properties that I have recently sold on a weekly or monthly basis. I would like the information to be displayed similarly to http://www.tobiaskellner.com/properties.html . I should be able to upload: picture, price, bldg size, lot size, closing date for each property. This will require a user friendly back end that I can navigate.

- On the home page, I also want to have a form where visitors can request a Market Analysis of their property by entering: Name, property address, email address, phone number. I will be sent an email with this information and I can follow up via telephone or email direct.

- The Harbinridge Team page will have a picture, contact info, and brief bio for each member of the team. I would like to be able to adjust this on a user friendly back end.

I have included my Company Logo. Feel free to use any text from my current website: www.movewithquorl.com. Also, any sleek looking stock photos of office / commercial buildings can be used for the initial design purposes.

I look forward to getting your design submittal and moving forward asap!

Target Market(s)

Los Angeles real estate brokers, developers, and investors.

Industry/Entity Type

Real Estate

Coding

Coded - Design and coding required

Number of Pages Required

5+ page

Font styles to use
Sans Serif

Colors
ffffff
85abd2
0455a3
b2b2b2
000000
3276b5

Requirements
Must have
• Sleek and professional design.
• - I want to make sure that we can imbed a news commercial real estate news feed from: http://www.bizplotwire.com/news/ on the website's home page, similar to how it is on tobiaskellner.com.
• - Sold Properties page will allow me to upload the following information on to the website so that I can add new properties that I have recently sold on a weekly or monthly basis. I would like the information to be displayed similarly to http://www.tobiaskellner.com/properties.html . I should be able to upload: picture, price, bldg size, lot size, closing date for each property. This will require a user friendly back end that I can navigate.
• - On the home page, I also want to have a form where visitors can request a Market Analysis of their property by entering: Name, property address, email address, phone number. I will be sent an email with this information and I can follow up via telephone or email direct.
Nice to have
• Dynamic banner on the home page with beautiful photos that change every few seconds.

```html
<!DOCTYPE html>
<html lang="en">
<head>
<meta charset="utf-8">
<title>Harbinridge Realty — Commercial Real Estate</title>
<link href="https://fonts.googleapis.com/css2?family=Poppins:wght@300;400;500;600;700&display=swap" rel="stylesheet">
<style>
:root{
  --blue:#0455a3;
  --sky:#1a9be3;
  --mid:#3276b5;
  --pale:#85abd2;
  --grey:#b2b2b2;
  --ink:#1d1f24;
  --text:#5b6068;
  --navy:#0f2558;
  --night:#0a1a3f;
  --light:#eef0f3;
  --foot:#232428;
  --white:#ffffff;
}
*{box-sizing:border-box;margin:0;padding:0}
html,body{width:1200px;height:4452px;overflow:hidden}
body{font-family:"Poppins",Arial,sans-serif;color:var(--ink);background:var(--white);position:relative}
.wrap{width:900px;margin:0 auto;position:relative}
section,header,footer{position:relative;overflow:hidden}

/* top bar */
.topbar{height:32px;background:#1c1f26;color:#aab0ba;font-size:11px;display:flex;align-items:center;justify-content:center;gap:28px}
.topbar span{display:flex;align-items:center;gap:6px}
.topbar i{width:6px;height:6px;border-radius:50%;background:var(--sky);display:inline-block}

/* nav */
.nav{height:44px;background:var(--white);display:flex;align-items:center;padding-left:160px;box-shadow:0 1px 4px rgba(0,0,0,.08);z-index:2}
.brand{display:flex;align-items:center;gap:8px;font-weight:700;font-size:17px;color:var(--blue);width:230px}
.brand b{width:12px;height:12px;background:var(--blue);display:inline-block}
.menu{display:flex;gap:26px;font-size:11px;font-weight:500;text-transform:uppercase;color:#4a4f58;margin-left:30px}
.menu .on{color:var(--sky);border-bottom:2px solid var(--sky);padding-bottom:3px}
.navphone{margin-left:auto;height:44px;width:250px;background:var(--blue);color:var(--white);display:flex;align-items:center;gap:10px;padding-left:30px;font-weight:600;font-size:15px}

/* hero */
.hero{height:548px;background:
  linear-gradient(180deg,rgba(255,255,255,0) 55%,rgba(40,52,70,.55) 100%),
  linear-gradient(90deg,#6f8aa8 0%,#9db4cc 22%,#5f7896 38%,#aabcd0 52%,#56708f 66%,#8aa2bd 80%,#4f6684 100%),
  linear-gradient(180deg,#d7e3ef 0%,#b3c6da 30%,#7890ab 65%,#4a5a6e 100%);
  background-blend-mode:normal,soft-light,normal}
.quote{position:absolute;left:762px;top:16px;width:378px;background:var(--white);box-shadow:0 4px 16px rgba(0,0,0,.2)}
.quote h2{background:var(--sky);color:var(--white);font-size:17px;font-weight:500;line-height:1.35;padding:16px 24px;text-align:center}
.quote form{padding:16px 22px 18px}
.field{height:32px;border:1px solid #d5d9df;font-size:11px;color:#9aa0a8;padding:0 10px;display:flex;align-items:center;margin-bottom:9px}
.captcha{display:flex;align-items:center;gap:8px;font-size:11px;color:#5b6068;height:42px;border:1px solid #d5d9df;background:#f8f9fa;padding:0 10px;margin:4px 0 12px;width:230px}
.captcha i{width:16px;height:16px;border:1px solid #9aa0a8;background:var(--white);display:inline-block}
.btn{display:inline-flex;align-items:center;gap:8px;background:var(--sky);color:var(--white);font-size:12px;font-weight:500;height:34px;padding:0 20px}

/* about */
.about{height:428px;display:flex}
.about .photo{width:580px;height:410px;background:linear-gradient(160deg,#dfe7ef 0%,#9fb3c8 45%,#6b8199 100%)}
.about .copy{padding:50px 40px 0 40px;width:580px;font-size:13px;line-height:1.85;color:var(--text)}
.about .btn{margin-top:26px}

/* headings */
.head{display:flex;align-items:center;justify-content:space-between}
.title{font-size:29px;font-weight:600;color:var(--ink);position:relative;padding-bottom:10px}
.title em{color:var(--sky);font-style:italic;font-weight:700;margin-right:6px}
.title:after{content:"";position:absolute;left:0;bottom:0;width:56px;height:3px;background:var(--sky)}
.light .title{color:var(--white)}
.ctrl{display:flex;gap:6px;align-items:center}
.ctrl span{width:26px;height:26px;display:flex;align-items:center;justify-content:center;background:#e4e7eb;color:#6b7079;font-size:12px}
.ctrl .act{background:var(--sky);color:var(--white)}
.ctrl .all{width:auto;padding:0 18px;background:#1f2228;color:var(--white);font-size:11px;height:26px;margin-left:10px}

/* sold */
.sold{height:532px;padding-top:52px}
.cards{display:flex;gap:21px;margin-top:34px}
.pcard{width:286px;background:var(--white);box-shadow:0 2px 8px rgba(0,0,0,.08)}
.pimg{height:150px}
.pcard h3{font-size:15px;font-weight:500;margin:12px 10px 2px}
.price{color:var(--sky);font-weight:600;font-size:15px;margin:0 10px 8px}
.meta{font-size:10px;color:#8a9099;margin:0 10px;line-height:1.8}
.meta b{display:inline-block;width:7px;height:7px;background:var(--pale);margin-right:6px}
.pbar{display:flex;margin-top:12px;height:30px}
.pbar span{flex:1;background:var(--sky);color:var(--white);font-size:10px;display:flex;align-items:center;justify-content:center;border-right:1px solid rgba(255,255,255,.35)}
.pbar .go{flex:0 0 38px;background:var(--blue);border:0}

/* types band */
.types{height:532px;margin-top:20px;background:linear-gradient(180deg,#16336f 0%,#0f2558 45%,#0a1a3f 100%);text-align:center;color:var(--white)}
.types p{font-size:15px;font-weight:300;line-height:1.6;margin-top:120px}
.icons{display:flex;justify-content:center;gap:46px;margin-top:36px}
.icon{width:84px;text-align:center;font-size:12px}
.icon .disc{width:84px;height:84px;border-radius:50%;background:var(--sky);border:4px solid rgba(255,255,255,.25);display:flex;align-items:center;justify-content:center;margin-bottom:12px}

/* team */
.team{height:460px;padding-top:56px}
.people{display:flex;gap:21px;margin-top:36px}
.person{width:208px}
.person .pic{height:190px;border:3px solid transparent}
.person.sel .pic{border-color:var(--sky)}
.person h4{font-size:16px;font-weight:500;margin-top:12px}
.person h4 span{color:var(--sky);font-weight:400}
.person p{font-size:11px;color:#8a9099}

/* contacts */
.contact{height:628px;background:linear-gradient(180deg,#1a3a82 0%,#12296a 50%,#0b1b48 100%);padding-top:80px}
.contact .title{margin:0 auto;display:table}
.cform{width:680px;margin:40px auto 0}
.row{display:flex;gap:30px;margin-bottom:12px}
.cin{flex:1;height:32px;background:var(--white);font-size:11px;color:#6b7079;padding:0 10px;display:flex;align-items:center}
.cmsg{height:130px;background:var(--white);font-size:11px;color:#6b7079;padding:8px 10px}
.cform .btn{display:flex;width:130px;margin:44px auto 0;justify-content:center}

/* news */
.news{height:710px;background:var(--light);padding-top:52px}
.ncard{width:286px}
.ncard .nimg{height:150px;border:3px solid transparent}
.ncard.sel .nimg{border-color:var(--sky)}
.ncard h3{font-size:14px;font-weight:700;line-height:1.45;margin-top:16px}
.ncard p{font-size:11px;line-height:1.7;color:#7a8089;margin-top:12px}
.news .btn{display:flex;width:150px;justify-content:center;margin:40px auto 0}

/* newsletter */
.letter{height:116px;background:var(--sky);display:flex;align-items:center;padding-left:150px;color:var(--white)}
.letter .lbl{display:flex;align-items:center;gap:14px;font-weight:600;font-size:14px;line-height:1.2;width:260px}
.letter .email{width:610px;border-bottom:1px solid rgba(255,255,255,.7);height:30px;font-size:11px;display:flex;align-items:center;justify-content:space-between}

/* footer */
.footer{height:318px;background:var(--foot);color:#b8bcc4}
.footbrand{position:absolute;left:150px;top:128px;display:flex;align-items:center;gap:10px;font-size:22px;font-weight:600;color:var(--white)}
.footbrand b{width:14px;height:14px;background:var(--sky);display:inline-block}
.fcol{position:absolute;top:40px}
.fcol h5{color:var(--white);font-size:15px;font-weight:500;margin-bottom:14px}
.fcol li{list-style:none;font-size:12px;line-height:2.1;display:flex;align-items:center;gap:8px}
.fcol li i{width:4px;height:4px;background:var(--sky);display:inline-block}
.fcol li.on{color:var(--sky)}
.fcol.info li{align-items:flex-start;line-height:1.7;margin-bottom:10px}
.fcol.info li svg{margin-top:3px;flex:none}
.bottom{height:52px;background:#18191c;color:#80858e;font-size:10px;display:flex;align-items:center;padding:0 150px;justify-content:space-between}
.bottom .dots{display:flex;gap:10px}
.bottom .dots i{width:14px;height:14px;border-radius:50%;background:#4a4d54;display:inline-block}
</style>
</head>
<body>

<div class="topbar"><span><i></i>(424) 555-0186</span><span><i></i>info@movewithquorl.com</span></div>

<header class="nav">
  <div class="brand"><b></b>Harbinridge Realty</div>
  <nav class="menu"><span class="on">Home</span><span>Services</span><span>Sold Properties</span><span>Harbinridge Team</span><span>Contact</span></nav>
  <div class="navphone">
    <svg width="16" height="16" viewBox="0 0 24 24" fill="#fff"><path d="M6.6 10.8a15 15 0 0 0 6.6 6.6l2.2-2.2a1 1 0 0 1 1-.25 11.4 11.4 0 0 0 3.6.57 1 1 0 0 1 1 1V20a1 1 0 0 1-1 1A17 17 0 0 1 3 4a1 1 0 0 1 1-1h3.5a1 1 0 0 1 1 1c0 1.25.2 2.45.57 3.57a1 1 0 0 1-.25 1z"/></svg>
    (424) 555-0186
  </div>
</header>

<section class="hero" role="img" aria-label="Banner photo: downtown Los Angeles skyline with glass high-rise office towers under a pale blue sky">
  <div class="quote">
    <h2>Request Market Analysis<br>For Your Property</h2>
    <form>
      <div class="field">Your Name</div>
      <div class="field">Property Address</div>
      <div class="field">Email</div>
      <div class="field">Phone Number</div>
      <div class="captcha"><i></i>I am not a robot</div>
      <span class="btn">Request
        <svg width="12" height="12" viewBox="0 0 24 24" fill="#fff"><path d="M2 21l21-9L2 3v7l15 2-15 2z"/></svg></span>
    </form>
  </div>
</section>

<section class="about">
  <div class="photo" role="img" aria-label="Aerial view of a city business district"></div>
  <div class="copy">
    Harbinridge Realty is a commercial real estate brokerage firm that provides a range of services to assist each of our clients in reaching their real estate objectives quickly and efficiently. Our focus on Southern California investment properties allows us to have a unique and focused perspective on this highly competitive market. Through our experience, diligence and resourcefulness, we help our clients make informed real estate decisions with their specific goals in mind.
    <br><span class="btn">Read More
      <svg width="10" height="10" viewBox="0 0 24 24" fill="#fff"><path d="M8 4l8 8-8 8z"/></svg></span>
  </div>
</section>

<section class="sold">
  <div class="wrap">
    <div class="head">
      <h2 class="title"><em>//</em>Sold Properties</h2>
      <div class="ctrl"><span>&#8249;</span><span class="act">&#8250;</span><span class="all">View All</span></div>
    </div>
    <div class="cards">
      <article class="pcard">
        <div class="pimg" role="img" aria-label="Single family house with front lawn" style="background:linear-gradient(160deg,#cfd9c6,#8fa38a)"></div>
        <h3>Single House Near Orlando</h3>
        <div class="price">$135,000</div>
        <div class="meta"><b></b>House<br><b></b>Harbor Point Ave, Los Angeles<br><b></b>October 12, 2017</div>
        <div class="pbar"><span>2,400 SqFt Bldg</span><span>5,800 SqFt Lot</span><span class="go">&#8594;</span></div>
      </article>
      <article class="pcard">
        <div class="pimg" role="img" aria-label="Corporate office building exterior" style="background:linear-gradient(160deg,#d7dde6,#8d9bb0)"></div>
        <h3>Corporate Office</h3>
        <div class="price">$92,233</div>
        <div class="meta"><b></b>Office<br><b></b>Wilcrest Blvd, Los Angeles<br><b></b>September 26, 2017</div>
        <div class="pbar"><span>8,200 SqFt Bldg</span><span>12,000 SqFt Lot</span><span class="go">&#8594;</span></div>
      </article>
      <article class="pcard">
        <div class="pimg" role="img" aria-label="Modern industrial building" style="background:linear-gradient(160deg,#e8ecf1,#a9b6c6)"></div>
        <h3>Industrial Building</h3>
        <div class="price">$322,000</div>
        <div class="meta"><b></b>Industrial<br><b></b>Canyon Mill Rd, Los Angeles<br><b></b>August 30, 2017</div>
        <div class="pbar"><span>18,500 SqFt Bldg</span><span>26,000 SqFt Lot</span><span class="go">&#8594;</span></div>
      </article>
    </div>
  </div>
</section>

<section class="types" role="img" aria-label="Night city skyline in deep blue tones behind property type icons">
  <p>Harbinridge Realty provides specialized<br>expertise in specific property types including:</p>
  <div class="icons">
    <div class="icon"><div class="disc"><svg width="36" height="36" viewBox="0 0 24 24" fill="#fff"><path d="M3 4h18l1 5H2zM4 10h16v10H4zm3 3v7h4v-7z"/></svg></div>Retail</div>
    <div class="icon"><div class="disc"><svg width="36" height="36" viewBox="0 0 24 24" fill="#fff"><path d="M2 20V10l6 4V10l6 4V4h4v16z"/></svg></div>Industrial</div>
    <div class="icon"><div class="disc"><svg width="36" height="36" viewBox="0 0 24 24" fill="#fff"><path d="M6 2h12v20H6zm3 3v2h2V5zm4 0v2h2V5zM9 9v2h2V9zm4 0v2h2V9zm-4 4v2h2v-2zm4 0v2h2v-2z"/></svg></div>Office</div>
    <div class="icon"><div class="disc"><svg width="36" height="36" viewBox="0 0 24 24" fill="#fff"><path d="M3 22V8h7V2h11v20zm3-11v2h2v-2zm0 4v2h2v-2zm7-10v2h2V5zm4 0v2h2V5zm-4 4v2h2V9zm4 0v2h2V9z"/></svg></div>Apartments</div>
    <div class="icon"><div class="disc"><svg width="36" height="36" viewBox="0 0 24 24" fill="#fff"><path d="M12 3l10 8h-3v10H5V11H2zm-2 11v7h4v-7z"/></svg></div>2–4 Units</div>
    <div class="icon"><div class="disc"><svg width="36" height="36" viewBox="0 0 24 24" fill="#fff"><path d="M2 20l7-11 4 6 3-4 6 9z"/></svg></div>Land</div>
  </div>
</section>

<section class="team">
  <div class="wrap">
    <div class="head">
      <h2 class="title"><em>//</em>Our Team</h2>
      <div class="ctrl"><span>&#8249;</span><span class="act">&#8250;</span><span class="all">View All</span></div>
    </div>
    <div class="people">
      <div class="person"><div class="pic" role="img" aria-label="Portrait of Dana Whitlock" style="background:linear-gradient(180deg,#d9dde2,#8f959d)"></div><h4><span>Dana</span> Whitlock</h4><p>President</p></div>
      <div class="person sel"><div class="pic" role="img" aria-label="Portrait of Nora Castell" style="background:linear-gradient(180deg,#e3dfd9,#a89c8e)"></div><h4><span>Nora</span> Castell</h4><p>Co-Founder</p></div>
      <div class="person"><div class="pic" role="img" aria-label="Portrait of Owen Ralstead" style="background:linear-gradient(180deg,#d6d9de,#80868f)"></div><h4><span>Owen</span> Ralstead</h4><p>Managing Director</p></div>
      <div class="person"><div class="pic" role="img" aria-label="Portrait of Miles Hartgrove" style="background:linear-gradient(180deg,#dcdfe3,#959ba3)"></div><h4><span>Miles</span> Hartgrove</h4><p>Account Manager</p></div>
    </div>
  </div>
</section>

<section class="contact light" role="img" aria-label="City skyline in dark blue tones behind the contact form">
  <h2 class="title"><em>//</em>Contacts</h2>
  <div class="cform">
    <div class="row"><div class="cin">Name</div><div class="cin">Email</div></div>
    <div class="row"><div class="cin">Phone No</div><div class="cin">Subject</div></div>
    <div class="cmsg">Message</div>
    <span class="btn">Submit
      <svg width="12" height="12" viewBox="0 0 24 24" fill="#fff"><path d="M2 21l21-9L2 3v7l15 2-15 2z"/></svg></span>
  </div>
</section>

<section class="news">
  <div class="wrap">
    <div class="head">
      <h2 class="title"><em>//</em>Latest Commercial R.E. News</h2>
      <div class="ctrl"><span>&#8249;</span><span class="act">&#8250;</span><span class="all">View All</span></div>
    </div>
    <div class="cards">
      <article class="ncard"><div class="nimg" role="img" aria-label="Waterfront residential tower" style="background:linear-gradient(160deg,#c8d6e2,#7f97ad)"></div>
        <h3>Veldran Holdings marks completion of second Kakaako tower</h3>
        <p>Veldran Holdings said on Wednesday it reached completion of its new tower and opened the residences to buyers.</p></article>
      <article class="ncard sel"><div class="nimg" role="img" aria-label="Executives at a press announcement" style="background:linear-gradient(160deg,#3f4b5e,#1e2633)"></div>
        <h3>Tech group Lumacorp picks Toronto for first digital neighborhood</h3>
        <p>Lumacorp said it will build a new urban district on the waterfront as a test for smart city planning.</p></article>
      <article class="ncard"><div class="nimg" role="img" aria-label="Office building street view" style="background:linear-gradient(160deg,#d9dde3,#9aa4b1)"></div>
        <h3>Ostrander Real Estate channels experience, creativity as it looks to the future</h3>
        <p>The firm said on Wednesday it plans to grow its team and expand into new markets next year.</p></article>
    </div>
    <span class="btn">Read All News
      <svg width="12" height="12" viewBox="0 0 24 24" fill="#fff"><path d="M2 21l21-9L2 3v7l15 2-15 2z"/></svg></span>
  </div>
</section>

<section class="letter">
  <div class="lbl">
    <svg width="34" height="34" viewBox="0 0 24 24" fill="none" stroke="#fff" stroke-width="1.5"><path d="M2 11l20-8-6 18-4-7z"/><path d="M12 14l10-11"/></svg>
    <span>OUR<br>NEWSLETTER</span>
  </div>
  <div class="email">Enter Your Email Address
    <svg width="14" height="14" viewBox="0 0 24 24" fill="#fff"><path d="M2 21l21-9L2 3v7l15 2-15 2z"/></svg></div>
</section>

<footer class="footer">
  <div class="footbrand"><b></b>Harbinridge Realty</div>
  <div class="fcol" style="left:580px">
    <h5>Quick Links</h5>
    <ul><li class="on"><i></i>Home</li><li><i></i>Services</li><li><i></i>Sold Properties</li><li><i></i>Harbinridge Team</li><li><i></i>Contact</li></ul>
  </div>
  <div class="fcol info" style="left:770px">
    <h5>Contact Info</h5>
    <ul>
      <li><svg width="12" height="12" viewBox="0 0 24 24" fill="#1a9be3"><path d="M12 2a7 7 0 0 0-7 7c0 5 7 13 7 13s7-8 7-13a7 7 0 0 0-7-7zm0 9.5A2.5 2.5 0 1 1 12 6.5a2.5 2.5 0 0 1 0 5z"/></svg>2217 Corvella Ave Ste 14<br>Los Angeles, CA 90025</li>
      <li><svg width="12" height="12" viewBox="0 0 24 24" fill="#1a9be3"><path d="M6.6 10.8a15 15 0 0 0 6.6 6.6l2.2-2.2a1 1 0 0 1 1-.25 11.4 11.4 0 0 0 3.6.57 1 1 0 0 1 1 1V20a1 1 0 0 1-1 1A17 17 0 0 1 3 4a1 1 0 0 1 1-1h3.5a1 1 0 0 1 1 1c0 1.25.2 2.45.57 3.57a1 1 0 0 1-.25 1z"/></svg><span style="color:#fff;font-weight:600">(424) 555-0186</span></li>
      <li><svg width="12" height="12" viewBox="0 0 24 24" fill="#1a9be3"><path d="M6.6 10.8a15 15 0 0 0 6.6 6.6l2.2-2.2a1 1 0 0 1 1-.25 11.4 11.4 0 0 0 3.6.57 1 1 0 0 1 1 1V20a1 1 0 0 1-1 1A17 17 0 0 1 3 4a1 1 0 0 1 1-1h3.5a1 1 0 0 1 1 1c0 1.25.2 2.45.57 3.57a1 1 0 0 1-.25 1z"/></svg><span style="color:#fff;font-weight:600">(424) 555-0142</span></li>
      <li><svg width="12" height="12" viewBox="0 0 24 24" fill="#1a9be3"><path d="M2 5h20v14H2zm2 2v.5l8 5 8-5V7l-8 5z"/></svg>dwhitlock@movewithquorl.com</li>
    </ul>
  </div>
</footer>

<div class="bottom"><span>© Copyright 2017 Harbinridge Realty. All rights reserved.</span><span class="dots"><i></i><i></i><i></i><i></i></span></div>

</body>
</html>
```